MGC Business Card Design

I am a wedding and event Planner. I have just completed a name change from Soirees by Lucette to The Gathering Corner and I just received my new logo and need new business cards to match my new brand. Elegant, chic and upscale yet simple. I am drafting a new website on my old (for drafting purposes). You can take a look and it will give you an idea of the direction of my brand. (www.soireesbylucette.example). I would like gray and white colors and it can be a shaded mixture of grays. I am open in regard to placement of the information

Target Market(s)

Brides, Corporate Companies, Families etc.

Industry/Entity Type

Wedding

Contact Information for Business Card

The Gathering Corner
www.mygatheringcorner.example
Event Planning and Design Firm
Lucette M. Harlow, Owner/CEO
Certified Event & Wedding Planner
T: (555) 214-7390 | F: (555) 307-4128
E: wegather@mygatheringcorner.example
(please put T, E & F letters in a script font)

Gather to Plan. Plan to Share. Share the Joy. (lh)

(social icons instead of text)
twitter: @gatheringcorner1
facebook: @thegatheringcorner
Pinterest: @gatheringcorner
instagram: @thegatheringcorner1

Can we put a barcode leading to my website

```html
<!DOCTYPE html>
<html lang="en">
<head>
<meta charset="utf-8">
<title>The Gathering Corner – Business Card</title>
<link rel="stylesheet" href="https://fonts.googleapis.com/css2?family=PT+Sans&family=PT+Serif&family=Great+Vibes&display=swap">
<style>
  :root {
    --stage: #1b1b1b;
    --card-white: #ffffff;
    --band-gray: #8e8e8e;
    --band-gray-light: #a3a3a3;
    --ink-dark: #4a4646;
    --ink-mid: #6b6b6b;
    --ink-on-band: #ffffff;
    --icon-dark: #5a5050;
    --faint: #e6e6e6;
  }
  * { box-sizing: border-box; margin: 0; padding: 0; }
  html, body { width: 1200px; height: 1000px; overflow: hidden; }
  body {
    background: var(--stage);
    font-family: "PT Sans", sans-serif;
    display: flex;
    flex-direction: column;
    align-items: center;
    justify-content: center;
    gap: 60px;
  }
  .card {
    position: relative;
    width: 700px;
    height: 400px;
    background: var(--card-white);
    overflow: hidden;
    box-shadow: 0 6px 24px rgba(0,0,0,.5);
  }

  /* ---------- front ---------- */
  .front .band {
    position: absolute; left: 0; right: 0; top: 150px; height: 220px;
    background: linear-gradient(180deg, var(--band-gray) 0%, var(--band-gray-light) 100%);
  }
  .brand {
    position: absolute; top: 26px; right: 48px;
    display: flex; align-items: center; gap: 18px;
  }
  .brand-circle {
    width: 62px; height: 62px; border-radius: 50%;
    border: 2px solid var(--ink-mid);
  }
  .brand-name {
    font-size: 30px; letter-spacing: 4px; color: var(--ink-mid);
    text-transform: uppercase;
  }
  .firm-line {
    position: absolute; top: 96px; right: 48px;
    font-family: "Great Vibes", cursive;
    font-size: 28px; color: var(--ink-mid);
  }
  .person {
    position: absolute; top: 166px; left: 44px; color: var(--ink-on-band);
  }
  .person-name { font-size: 26px; }
  .person-title { font-size: 14px; margin-top: 4px; }
  .contact-list {
    position: absolute; top: 254px; left: 44px; list-style: none;
    color: var(--ink-on-band); font-size: 20px;
  }
  .contact-list li { display: flex; align-items: center; gap: 14px; margin-bottom: 8px; }
  .contact-mark {
    width: 26px; height: 26px; border-radius: 50%;
    background: var(--card-white); color: var(--ink-mid);
    font-family: "Great Vibes", cursive; font-size: 19px; line-height: 1;
    display: flex; align-items: center; justify-content: center;
  }

  /* ---------- back ---------- */
  .back .band {
    position: absolute; left: 0; right: 0; top: 0; height: 130px;
    background: linear-gradient(180deg, var(--band-gray-light) 0%, var(--band-gray) 100%);
    color: var(--ink-on-band); text-align: center;
  }
  .website { font-size: 22px; margin-top: 30px; letter-spacing: .5px; }
  .tagline { font-family: "PT Serif", serif; font-size: 26px; margin-top: 8px; }
  .back .foot {
    position: absolute; left: 0; right: 0; bottom: 0; height: 22px;
    background: var(--band-gray);
  }
  .social-list {
    position: absolute; top: 160px; left: 44px; list-style: none;
    font-size: 20px; color: var(--ink-dark);
  }
  .social-list li { display: flex; align-items: center; gap: 14px; margin-bottom: 8px; }
  .social-dot {
    width: 22px; height: 22px; border-radius: 50%; background: var(--icon-dark);
  }
  .faint-mark {
    position: absolute; right: 60px; bottom: 40px;
    width: 150px; height: 150px; border-radius: 50%;
    border: 2px solid var(--faint);
  }
</style>
</head>
<body>

  <section class="card front" aria-label="Business card front">
    <div class="band"></div>
    <div class="brand">
      <span class="brand-circle"></span>
      <span class="brand-name">The Gathering Corner</span>
    </div>
    <p class="firm-line">Event Planning and Design Firm</p>
    <div class="person">
      <p class="person-name">Lucette M. Harlow</p>
      <p class="person-title">Owner/CEO Certified Event &amp; Wedding Planner</p>
    </div>
    <ul class="contact-list">
      <li><span class="contact-mark">T</span>(555) 214-7390</li>
      <li><span class="contact-mark">F</span>(555) 307-4128</li>
      <li><span class="contact-mark">E</span>wegather@mygatheringcorner.example</li>
    </ul>
  </section>

  <section class="card back" aria-label="Business card back">
    <div class="band">
      <p class="website">www.mygatheringcorner.example</p>
      <p class="tagline">Gather to Plan. Plan to Share. Share the Joy.</p>
    </div>
    <ul class="social-list">
      <li><span class="social-dot"></span>gatheringcorner1</li>
      <li><span class="social-dot"></span>thegatheringcorner</li>
      <li><span class="social-dot"></span>gatheringcorner</li>
      <li><span class="social-dot"></span>thegatheringcorner1</li>
    </ul>
    <div class="faint-mark" role="img" aria-label="Faint brand emblem"></div>
    <div class="foot"></div>
  </section>

</body>
</html>
```